exclusive Speakeasy Bar Web design in New Jersey USA

We are opening a speakeasy in New Jersey USA soon. we are looking for a web designer to do our web site including the coding. we a looking for a 4 to 5 page web design. the site will be mostly static. home page, contact page, menu page and a link to a 3rd party site (most likely Qelmo) for reservations. we are looking for this designer to do our menu deign as well. we are looking for a quick turnaround 7-10 days. i am attaching some pictures for the designers to see the concept design and the actual current pictures with our logo as well. professionally taken pictures will be provided later on. our photographer will be taking the pictures in the next week.

Industry/Entity Type

Restaurant, Bar, Speakeasy

Coding

Coded - Design and coding required

Number of Pages Required

4 page

Requirements
Must have
• home page, contact page, menu page and a link to qelmo.com for reservations
Nice to have
• some videos

```html
<!DOCTYPE html>
<html lang="en">
<head>
<meta charset="utf-8">
<title>Velvet Key — New Jersey Speakeasy</title>
<link rel="stylesheet" href="https://fonts.googleapis.com/css2?family=Cinzel:wght@400;700&family=Inter:wght@400;600&display=swap">
<style>
:root{
  --ink:#1f1b18;
  --ink-deep:#070605;
  --panel:#2b2521;
  --gold:#c9993a;
  --gold-soft:#a8823f;
  --text:#e9e3da;
  --muted:#b9b0a4;
}
*{box-sizing:border-box;margin:0;padding:0}
html,body{width:1200px;height:3596px;overflow:hidden;background:var(--ink-deep)}
body{font-family:"Inter",sans-serif;color:var(--text)}
.page{position:relative;width:1200px;height:3596px;overflow:hidden;
  background:linear-gradient(180deg,var(--ink) 0,#1c1815 1479px,var(--ink-deep) 1480px,var(--ink-deep) 3062px,#17130f 3200px,#0c0a08 3596px)}
.abs{position:absolute}
.serif{font-family:"Cinzel",serif;font-weight:400}
.center{left:0;width:1200px;text-align:center}

/* hero */
.hero-photo{left:0;top:0;width:1200px;height:725px;
  background:radial-gradient(ellipse at 50% 40%,#4a3a2b 0,#2d241c 45%,#15110d 100%);
  clip-path:polygon(0 0,1200px 0,1200px 530px,600px 723px,0 530px)}
.nav a{position:absolute;top:38px;font-family:"Cinzel",serif;font-size:17px;color:var(--text);text-decoration:none;letter-spacing:.5px}
.social{display:flex;gap:12px}
.social span{width:14px;height:14px;border:1.5px solid var(--gold);border-radius:50%;display:block}
.logo-box{border:2px solid var(--gold);display:flex;flex-direction:column;align-items:center;justify-content:center;color:var(--text);font-family:"Cinzel",serif}
.welcome{top:366px;font-size:25px;letter-spacing:1px}
.brand-title{top:398px;font-size:82px;font-weight:700;letter-spacing:2px;color:#f4efe8}
.tagline{top:514px;font-size:15px;color:var(--text)}
.btn{display:block;color:var(--gold);text-decoration:none;font-family:"Cinzel",serif;font-size:21px;text-align:center}
.btn svg{position:absolute;left:0;top:0}
.btn span{position:relative}

/* sections */
.section-title{font-size:41px;letter-spacing:1px;color:#f1ebe2}
.lead{top:897px;font-size:15px;font-weight:600}
.about-copy{left:262px;width:676px;top:935px;font-size:14.5px;line-height:23px;text-align:center;color:var(--muted)}
.read-more{top:1068px;font-family:"Cinzel",serif;font-size:16px;color:var(--gold-soft)}
.pattern{left:0;top:640px;width:1200px;height:840px;
  background:linear-gradient(180deg,rgba(255,255,255,0) 0,rgba(201,153,58,.04) 50%,rgba(0,0,0,.15) 100%)}
.panel{background:var(--panel)}
.h2{font-size:42px;line-height:55px;color:#f1ebe2}
.body-copy{font-size:14px;line-height:23px;color:var(--muted)}
.video{left:494px;top:1191px;width:597px;height:445px;border:5px solid #48413b;
  background:radial-gradient(circle at 50% 45%,#8a5a2e 0,#4b3220 40%,#1d150f 100%)}
.play{left:735px;top:1368px;width:104px;height:104px;border-radius:50%;border:4px solid var(--gold);background:rgba(120,90,50,.55)}
.photo{top:1929px;width:305px;height:422px}
.arrow{width:60px;height:60px;border-radius:50%;border:1.5px solid var(--gold);background:#000}
.follow{top:2409px;font-family:"Cinzel",serif;font-size:16px;color:var(--gold-soft)}
.footer h4{font-family:"Cinzel",serif;font-weight:400;font-size:15px;color:var(--text)}
.footer h4::after{content:"";display:block;margin-top:6px;width:90px;height:1px;background:var(--gold)}
.footer li{list-style:none;font-size:12px;color:var(--muted)}
.copyright{top:3411px;font-size:12px;color:var(--muted)}
</style>
</head>
<body>
<main class="page">

  <!-- Hero -->
  <div class="abs hero-photo" role="img" aria-label="Dimly lit back bar with shelves of liquor bottles"></div>
  <svg class="abs" style="left:0;top:520px" width="1200" height="215" aria-hidden="true">
    <polyline points="0,10 600,203 1200,10" fill="none" stroke="var(--gold)" stroke-width="3"/>
  </svg>

  <nav class="nav">
    <a href="#" style="left:217px">HOME</a>
    <a href="#" style="left:376px">MENU</a>
    <a href="#" style="left:535px">GALLERY</a>
    <a href="#" style="left:716px">CONTACT</a>
    <div class="abs social" style="left:908px;top:42px" aria-label="Social links"><span></span><span></span><span></span></div>
  </nav>

  <div class="abs logo-box" style="left:519px;top:123px;width:158px;height:206px">
    <span style="font-size:40px;font-weight:700;line-height:1">VELVET</span>
    <span style="font-size:40px;font-weight:700;line-height:1.1">KEY</span>
  </div>

  <p class="abs center serif welcome">WELCOME TO</p>
  <h1 class="abs center serif brand-title">VELVET KEY</h1>
  <p class="abs center tagline">Discover a Hidden Gem in <strong>New Jersey's</strong> Exclusive Speakeasy Scene</p>

  <a class="abs btn" href="https://qelmo.com" style="left:476px;top:567px;width:248px;height:66px;line-height:66px">
    <svg width="248" height="66" aria-hidden="true"><g fill="none" stroke="var(--gold)" stroke-width="2">
      <polyline points="38,5 244,5 244,34"/><polyline points="3,26 3,61 210,61"/>
      <rect x="2" y="2" width="13" height="13"/><rect x="232" y="48" width="13" height="13"/></g>
      <rect x="6" y="6" width="5" height="5" fill="var(--gold)"/><rect x="236" y="52" width="5" height="5" fill="var(--gold)"/></svg>
    <span>BOOK A VISIT</span>
  </a>

  <!-- About -->
  <div class="abs pattern" aria-hidden="true"></div>
  <h2 class="abs center serif section-title" style="top:785px">ABOUT US</h2>
  <p class="abs center lead">Experience the excitement of a Prohibition era Speakeasy bar in the heart of New Jersey.</p>
  <p class="abs about-copy">Indulge in handcrafted cocktails and immerse yourself in the nostalgic charm of the Roaring Twenties. Our attentive staff offers impeccable service reflective of the glamour and elegance of the bygone era. Enjoy classic and innovative libations while live music sets the ambiance for a night of extraordinary indulgence. Join us for an unforgettable experience and discover where the spirit of the 1920s lives on.</p>
  <p class="abs center read-more">READ MORE &nbsp;<svg width="36" height="10" aria-hidden="true"><path d="M0 5H34M29 1L34 5L29 9" fill="none" stroke="var(--gold)" stroke-width="1.2"/></svg></p>

  <!-- Step inside -->
  <div class="abs panel" style="left:110px;top:1288px;width:1090px;height:390px"></div>
  <h2 class="abs serif h2" style="left:179px;top:1336px">STEP INSIDE<br>VELVET KEY</h2>
  <svg class="abs" style="left:138px;top:1433px" width="135" height="45" aria-hidden="true"><g fill="none" stroke="var(--gold)" stroke-width="1.5"><path d="M14 0V40M7 27H112M120 27H134"/><rect x="1" y="32" width="12" height="12"/></g></svg>
  <p class="abs body-copy" style="left:179px;top:1482px;width:280px">Embark on a journey to the hidden world of Velvet Key. Watch as we reveal the captivating atmosphere, exquisite cocktails, and the undeniable charm that makes our bar a must-visit destination.</p>
  <div class="abs video" role="img" aria-label="Video still: bartender pouring a red cocktail at the bar"></div>
  <div class="abs play" aria-label="Play video"><svg width="96" height="96" aria-hidden="true"><path d="M38 30L66 48L38 66Z" fill="none" stroke="#f4efe8" stroke-width="4" stroke-linejoin="round"/></svg></div>

  <!-- Gallery -->
  <h2 class="abs center serif section-title" style="top:1808px">PHOTO GALLERY</h2>
  <div class="abs photo" style="left:116px;background:linear-gradient(160deg,#6b2a22,#22253a 55%,#101018)" role="img" aria-label="Bartender straining a martini"></div>
  <div class="abs photo" style="left:448px;background:linear-gradient(160deg,#9a8a6a,#5f6b3e 50%,#2a2418)" role="img" aria-label="Glasses of mojito raised in a toast"></div>
  <div class="abs photo" style="left:780px;background:linear-gradient(160deg,#c79a5c,#1f4a4c 50%,#3a2310)" role="img" aria-label="Wine glasses on a table beside teal booth seating"></div>
  <div class="abs arrow" style="left:84px;top:2111px"><svg width="58" height="58" aria-hidden="true"><path d="M41 29H17M24 22L17 29L24 36" fill="none" stroke="#fff" stroke-width="1.8"/></svg></div>
  <div class="abs arrow" style="left:1055px;top:2111px"><svg width="58" height="58" aria-hidden="true"><path d="M17 29H41M34 22L41 29L34 36" fill="none" stroke="#fff" stroke-width="1.8"/></svg></div>
  <p class="abs center follow">FOLLOW US ON &nbsp;<span style="display:inline-block;width:13px;height:13px;border:1.5px solid var(--gold);border-radius:50%;vertical-align:-1px"></span></p>

  <!-- Reserve -->
  <div class="abs panel" style="left:847px;top:2553px;width:353px;height:509px"></div>
  <div class="abs" style="left:624px;top:2607px;width:450px;height:409px;background:radial-gradient(circle at 30% 30%,#b8824a,#5a4633 45%,#2a2018)" role="img" aria-label="Table set with plates, candle and a Reserved card"></div>
  <svg class="abs" style="left:1055px;top:2576px" width="50" height="130" aria-hidden="true"><g fill="none" stroke="var(--gold)" stroke-width="1.5"><path d="M0 20H32V120"/><rect x="32" y="8" width="12" height="12"/></g></svg>
  <h2 class="abs serif h2" style="left:123px;top:2677px">RESERVE YOUR<br>SPOT AT VELVET KEY</h2>
  <p class="abs body-copy" style="left:123px;top:2803px;width:385px;font-size:15px">Step back in time and reserve your spot at NJ's exclusive speakeasy for an elegant and unforgettable night of mystery and timeless memories.</p>
  <a class="abs btn" href="https://qelmo.com" style="left:121px;top:2907px;width:248px;height:66px;line-height:66px">
    <svg width="248" height="66" aria-hidden="true"><g fill="none" stroke="var(--gold)" stroke-width="2">
      <polyline points="38,5 244,5 244,34"/><polyline points="3,26 3,61 210,61"/>
      <rect x="2" y="2" width="13" height="13"/><rect x="232" y="48" width="13" height="13"/></g>
      <rect x="6" y="6" width="5" height="5" fill="var(--gold)"/><rect x="236" y="52" width="5" height="5" fill="var(--gold)"/></svg>
    <span>BOOK A VISIT</span>
  </a>

  <!-- Footer -->
  <footer class="footer">
    <div class="abs logo-box" style="left:146px;top:3174px;width:93px;height:118px">
      <span style="font-size:19px;font-weight:700">VELVET</span><span style="font-size:19px;font-weight:700">KEY</span>
    </div>
    <p class="abs serif" style="left:144px;top:3324px;font-size:14px">FOLLOW US</p>
    <div class="abs social" style="left:146px;top:3354px" aria-label="Social links"><span></span><span></span><span></span></div>

    <div class="abs" style="left:400px;top:3170px">
      <h4>QUICK LINKS</h4>
      <ul style="margin-top:16px;display:grid;row-gap:12px"><li>Home</li><li>Menu</li><li>Contact</li><li>Terms and Conditions</li><li>Privacy policy</li></ul>
    </div>

    <div class="abs" style="left:589px;top:3171px">
      <h4>CONTACT</h4>
      <ul style="margin-top:16px;display:grid;row-gap:12px">
        <li style="display:flex;gap:12px"><svg width="12" height="14" aria-hidden="true"><path d="M6 13C2 8 1 6 1 5A5 5 0 0 1 11 5C11 6 10 8 6 13Z" fill="var(--gold)"/><circle cx="6" cy="5" r="1.8" fill="#111"/></svg><span>57 Larkspur Row, Hoboken,<br>New Jersey 07030</span></li>
        <li style="display:flex;gap:12px"><svg width="12" height="12" aria-hidden="true"><path d="M2 1L5 1L6 4L4 5C5 7 6 8 8 9L9 7L12 8V11C6 11 1 6 1 1Z" fill="var(--gold)"/></svg><span>(201) 555-0148</span></li>
        <li style="display:flex;gap:12px"><svg width="12" height="10" aria-hidden="true"><rect x="0" y="1" width="12" height="8" fill="var(--gold)"/><path d="M0 1L6 5L12 1" fill="none" stroke="#111"/></svg><span>hello@velvetkeybar.com</span></li>
      </ul>
    </div>

    <div class="abs" style="left:830px;top:3167px">
      <h4>OPENING HOURS</h4>
      <ul style="margin-top:16px;display:grid;row-gap:12px">
        <li style="display:flex;gap:12px;font-size:13px"><svg width="14" height="14" aria-hidden="true"><circle cx="7" cy="7" r="6" fill="none" stroke="var(--gold)" stroke-width="1.5"/><path d="M7 3V7H10" fill="none" stroke="var(--gold)" stroke-width="1.5"/></svg>Monday – Thursday: 5 pm – Midnight</li>
        <li style="display:flex;gap:12px;font-size:13px"><svg width="14" height="14" aria-hidden="true"><circle cx="7" cy="7" r="6" fill="none" stroke="var(--gold)" stroke-width="1.5"/><path d="M7 3V7H10" fill="none" stroke="var(--gold)" stroke-width="1.5"/></svg>Friday &amp; Saturday: 4 pm – 2 am</li>
        <li style="display:flex;gap:12px;font-size:13px"><svg width="14" height="14" aria-hidden="true"><circle cx="7" cy="7" r="6" fill="none" stroke="var(--gold)" stroke-width="1.5"/><path d="M7 3V7H10" fill="none" stroke="var(--gold)" stroke-width="1.5"/></svg>Sunday: 4 pm – Midnight</li>
      </ul>
    </div>

    <p class="abs center copyright">Copyright Velvet Key | All rights reserved</p>
  </footer>
</main>
</body>
</html>
```